Promo Flyer to put in prize bags at carnival

I am owner of Copper & Lark Hair Salon located in Gahanna, OH. I’m sponsoring a community carnival when I will be putting flyers in all attendees prize bags. This flyer will communicate details of my salon on one side (picture of me, logo, description of business, address, website, email, phone #) and the other side will showcase and a 50% discount for first time customers. Flyer can be 5” x 7” or greater

Side 1 details:
-Logo will be attached to this brief
-picture of me will be attached to this brief
-address: 2561 W. Pellward Ave, Suite 17, Fernhollow, ST, 00417
-website: clhairstudio.example
-email: Dorian.welby@clhairstudio.example
-phone: 555-52-BOOKS (26657)

Side 2 details:
-‘Guess what? You get 50% off your 1st service at Copper & Lark Hair Salon.’
-‘Expires 7/31/2018’
-Hair | Fashion | Photography
-Visit clhairstudio.example to book your service
-must present this flyer at time of service to receive discount

Hair And Beauty

Other font styles liked:
• Inoxida

Colors
3176b5
000000
ffffff

Must have
• 2 sides
• Color scheme to match logo

```html
<!DOCTYPE html>
<html lang="en">
<head>
<meta charset="utf-8">
<title>Copper &amp; Lark Hair Salon – Promo Flyer</title>
<link href="https://fonts.googleapis.com/css2?family=Great+Vibes&family=Merriweather:ital,wght@0,400;1,700&display=swap" rel="stylesheet">
<style>
  :root {
    --gold: #e8b03c;
    --sky: #00b9e8;
    --steel: #4a90c8;
    --charcoal: #3f4447;
    --ink: #1d1d1d;
    --white: #ffffff;
    --pink: #ee6fa8;
  }
  * { box-sizing: border-box; margin: 0; padding: 0; }
  html, body { width: 1200px; height: 1062px; overflow: hidden; background: var(--white); }
  .canvas { position: relative; width: 1200px; height: 1062px; }
  .flyer { position: absolute; top: 141px; width: 474px; height: 663px; overflow: hidden; }
  .flyer--front { left: 94px; }
  .flyer--back { left: 638px; background: var(--charcoal); }
  .flyer svg.shapes { position: absolute; inset: 0; width: 100%; height: 100%; }
  .script { font-family: "Great Vibes", cursive; color: var(--white); font-weight: 400; }
  .serif { font-family: "Merriweather", serif; }

  .brand { position: absolute; left: 0; right: 0; top: 318px; text-align: center; }
  .brand__name { font-size: 62px; line-height: 1; }
  .brand__tagline { display: flex; align-items: center; justify-content: center; gap: 8px; margin-top: 2px; font-size: 22px; }
  .brand__tagline::before, .brand__tagline::after { content: ""; width: 28px; height: 1px; background: var(--white); }

  .contact { position: absolute; left: 24px; top: 574px; list-style: none; font-size: 10.5px; line-height: 12.8px; color: var(--ink); }
  .contact li { display: flex; gap: 7px; }
  .contact svg { width: 9px; height: 9px; margin-top: 2px; flex: none; }

  .headline { position: absolute; left: 26px; top: 24px; font-size: 58px; line-height: 1; }
  .offer { position: absolute; right: 53px; top: 380px; text-align: right; }
  .offer__big { font-size: 56px; line-height: 1; }
  .offer__sub { font-style: italic; font-weight: 700; font-size: 12.5px; color: var(--gold); margin-top: 6px; }
  .details { position: absolute; right: 76px; top: 480px; text-align: right; font-size: 12.5px; line-height: 14.5px; color: var(--white); }
  .details-rule { position: absolute; left: 406px; top: 482px; width: 2px; height: 56px; background: var(--gold); }
  .disclaimer { position: absolute; left: 22px; top: 640px; font-size: 7.5px; color: var(--ink); }
  .badge { position: absolute; left: 291px; top: 228px; width: 122px; height: 122px; display: flex; align-items: center; justify-content: center; text-align: center; font-size: 24px; line-height: 0.95; color: var(--gold); }
</style>
</head>
<body>
<main class="canvas">

  <section class="flyer flyer--front">
    <svg class="shapes" viewBox="0 0 593 830" preserveAspectRatio="none">
      <defs>
        <linearGradient id="portrait-tone" x1="0" y1="0" x2="1" y2="1">
          <stop offset="0" stop-color="#8a8782"/>
          <stop offset="0.5" stop-color="#2f6a7e"/>
          <stop offset="1" stop-color="#5d5f61"/>
        </linearGradient>
      </defs>
      <rect width="593" height="830" fill="url(#portrait-tone)" role="img" aria-label="Photo of the salon owner in a teal suit and sunglasses"/>
      <polygon points="0,0 127,0 0,107" fill="var(--gold)"/>
      <polygon points="127,0 378,0 593,214 593,224" fill="var(--sky)"/>
      <polygon points="378,0 593,0 593,214" fill="var(--gold)"/>
      <polygon points="290,735 593,790 593,830 452,830" fill="var(--sky)"/>
      <polygon points="0,564 452,830 0,830" fill="var(--gold)"/>
      <polygon points="540,830 593,782 593,830" fill="var(--gold)"/>
    </svg>
    <div class="brand script">
      <div class="brand__name">Copper &amp; Lark</div>
      <div class="brand__tagline">An experience out of this world</div>
    </div>
    <ul class="contact serif">
      <li><svg viewBox="0 0 10 10"><path d="M5 0a3.5 3.5 0 0 0-3.5 3.5C1.5 6 5 10 5 10s3.5-4 3.5-6.5A3.5 3.5 0 0 0 5 0zm0 5a1.4 1.4 0 1 1 0-2.8A1.4 1.4 0 0 1 5 5z" fill="var(--ink)"/></svg><span>2561 W. Pellward Ave,<br>Suite 17, Fernhollow, ST, 00417</span></li>
      <li><svg viewBox="0 0 10 10"><circle cx="5" cy="5" r="4.3" fill="none" stroke="var(--ink)" stroke-width="1.2"/><path d="M0.7 5h8.6M5 0.7c-2.4 2.6-2.4 6 0 8.6M5 0.7c2.4 2.6 2.4 6 0 8.6" stroke="var(--ink)" stroke-width="0.9" fill="none"/></svg><span>www.clhairstudio.example</span></li>
      <li><svg viewBox="0 0 10 10"><rect x="0.6" y="1.6" width="8.8" height="6.8" fill="none" stroke="var(--ink)" stroke-width="1.1"/><path d="M0.6 1.6 5 5.6 9.4 1.6" fill="none" stroke="var(--ink)" stroke-width="1.1"/></svg><span>Dorian.welby@clhairstudio.example</span></li>
      <li><svg viewBox="0 0 10 10"><path d="M2.2 0.5 3.9 2.9 2.9 4a6 6 0 0 0 3.1 3.1l1.1-1 2.4 1.7-1.1 1.7C4.8 9.4 0.6 5.2 0.5 1.6z" fill="var(--ink)"/></svg><span>555-52-BOOKS (26657)</span></li>
    </ul>
  </section>

  <section class="flyer flyer--back">
    <svg class="shapes" viewBox="0 0 593 830" preserveAspectRatio="none">
      <defs>
        <linearGradient id="portrait-tone-2" x1="0" y1="0" x2="0" y2="1">
          <stop offset="0" stop-color="#6f6c68"/>
          <stop offset="1" stop-color="#2e5f70"/>
        </linearGradient>
      </defs>
      <polygon points="100,145 230,150 150,320 70,405 120,290" fill="var(--sky)"/>
      <polygon points="360,135 468,110 490,170 455,300 410,270" fill="var(--steel)"/>
      <polygon points="380,430 450,440 460,465 400,465" fill="var(--sky)"/>
      <polygon points="355,120 388,100 390,130" fill="var(--sky)"/>
      <polygon points="248,125 276,125 262,143" fill="var(--pink)"/>
      <polygon points="135,140 160,142 148,162" fill="var(--gold)"/>
      <polygon points="105,190 118,205 100,210" fill="var(--gold)"/>
      <polygon points="460,135 480,135 470,155" fill="var(--gold)"/>
      <polygon points="80,310 95,325 78,330" fill="var(--sky)"/>
      <polygon points="140,435 152,440 142,450" fill="var(--gold)"/>
      <polygon points="500,445 512,450 500,460" fill="var(--steel)"/>
      <circle cx="280" cy="304" r="164" fill="none" stroke="var(--gold)" stroke-width="22"/>
      <circle cx="280" cy="304" r="153" fill="url(#portrait-tone-2)" role="img" aria-label="Photo of the salon owner in sunglasses and a teal suit"/>
      <circle cx="440" cy="361" r="74" fill="#2d3235" stroke="var(--gold)" stroke-width="8"/>
      <polygon points="0,570 452,830 0,830" fill="var(--gold)"/>
      <polygon points="188,680 593,782 593,830 452,830" fill="var(--sky)"/>
      <polygon points="468,749 593,672 593,782" fill="var(--gold)"/>
    </svg>
    <h1 class="headline script">Guess what?</h1>
    <div class="badge script">Copper<br>&amp; Lark</div>
    <div class="offer">
      <div class="offer__big script">You get 50% off</div>
      <div class="offer__sub serif">your 1st service at Copper &amp; Lark Hair Salon.</div>
    </div>
    <div class="details serif">Expires 7/31/2018<br>Hair | Fashion | Photography<br>Visit clhairstudio.example<br>to book your service</div>
    <div class="details-rule"></div>
    <ul class="contact serif">
      <li><svg viewBox="0 0 10 10"><path d="M5 0a3.5 3.5 0 0 0-3.5 3.5C1.5 6 5 10 5 10s3.5-4 3.5-6.5A3.5 3.5 0 0 0 5 0zm0 5a1.4 1.4 0 1 1 0-2.8A1.4 1.4 0 0 1 5 5z" fill="var(--ink)"/></svg><span>2561 W. Pellward Ave,<br>Suite 17, Fernhollow, ST, 00417</span></li>
      <li><svg viewBox="0 0 10 10"><circle cx="5" cy="5" r="4.3" fill="none" stroke="var(--ink)" stroke-width="1.2"/><path d="M0.7 5h8.6M5 0.7c-2.4 2.6-2.4 6 0 8.6M5 0.7c2.4 2.6 2.4 6 0 8.6" stroke="var(--ink)" stroke-width="0.9" fill="none"/></svg><span>www.clhairstudio.example</span></li>
      <li><svg viewBox="0 0 10 10"><rect x="0.6" y="1.6" width="8.8" height="6.8" fill="none" stroke="var(--ink)" stroke-width="1.1"/><path d="M0.6 1.6 5 5.6 9.4 1.6" fill="none" stroke="var(--ink)" stroke-width="1.1"/></svg><span>Dorian.welby@clhairstudio.example</span></li>
      <li><svg viewBox="0 0 10 10"><path d="M2.2 0.5 3.9 2.9 2.9 4a6 6 0 0 0 3.1 3.1l1.1-1 2.4 1.7-1.1 1.7C4.8 9.4 0.6 5.2 0.5 1.6z" fill="var(--ink)"/></svg><span>555-52-BOOKS (26657)</span></li>
    </ul>
    <p class="disclaimer serif">Must present this flyer at time of service to receive discount</p>
  </section>

</main>
</body>
</html>
```